Driving School Business card design

Hi, we are starting a new business (Driving School) and would like your help with our business card design.
We are located in Adelaide SA.
Our aim is to help young people achieve best possible results by promoting safe and stress free driving.

Name of our school is "Brindle" which means best or most favorable.

Hope there is someone out there in wonderful world of design who can think outside of square and give us recognizable/ unique business card design.

Target Market(s)

16+

Industry/Entity Type

Business

Contact Information for Business Card

Name of our business is "Brindle driver training"
Our idea is to make letter "L' in Brindle more distinct (noticeable) by different color or font, so it gets associated with learner driver.
We like combination of white, dark gray and yellow but do not limit our self to that.
Reverse side of our card would have to incorporate writing space for date and time of the next lesson.

Requirements
Must have
• Business name: Brindle driver training
• Owner/ instructor name
• Mobile no:
• Loopnest logo
Should not have
• Anything Not associated with driving

```html
<!DOCTYPE html>
<html lang="en">
<head>
<meta charset="utf-8">
<title>Brindle Driver Training – Lesson Card</title>
<link rel="stylesheet" href="https://fonts.googleapis.com/css2?family=Open+Sans:ital,wght@0,400;0,700;1,700;1,800&display=swap">
<style>
  :root {
    --paper: #ffffff;
    --ink: #000000;
    --title-grey: #9a9a9a;
    --signal-yellow: #f7f200;
    --plate-yellow: #ffec00;
    --hill-green: #5f6b45;
    --road-grey: #6f7880;
    --grass-gold: #8c7d58;
    --shadow: rgba(0, 0, 0, 0.35);
  }
  * { margin: 0; padding: 0; box-sizing: border-box; }
  html, body {
    width: 1200px;
    height: 763px;
    overflow: hidden;
    background: var(--paper);
  }
  .card {
    position: relative;
    width: 1200px;
    height: 763px;
    overflow: hidden;
    background: var(--paper);
    font-family: "Open Sans", Arial, sans-serif;
  }
  .road-scene {
    position: absolute;
    inset: 0;
    background:
      radial-gradient(ellipse at 90% 20%, #3f5a2e 0%, transparent 45%),
      radial-gradient(ellipse at 60% 72%, var(--road-grey) 0%, transparent 40%),
      linear-gradient(160deg, var(--hill-green) 0%, var(--road-grey) 55%, var(--grass-gold) 100%);
  }
  .sweep {
    position: absolute;
    inset: 0;
    width: 1200px;
    height: 763px;
    filter: drop-shadow(6px 6px 10px var(--shadow));
  }
  .brand-title {
    position: absolute;
    left: 48px;
    top: 28px;
    font-size: 57px;
    font-weight: 800;
    font-style: italic;
    color: var(--title-grey);
    letter-spacing: -0.5px;
    line-height: 1;
  }
  .lesson-table {
    position: absolute;
    left: 48px;
    top: 125px;
    width: 1028px;
    border-collapse: collapse;
    box-shadow: 10px 14px 22px var(--shadow);
    background: var(--paper);
  }
  .lesson-table th {
    height: 66px;
    background: var(--ink);
    color: var(--signal-yellow);
    font-weight: 400;
    font-size: 34px;
    text-align: center;
    border: 3px solid var(--ink);
  }
  .lesson-table td {
    height: 63px;
    border: 4px solid var(--ink);
    background: var(--paper);
  }
  .col-lesson { width: 376px; }
  .col-date { width: 349px; }
  .col-time { width: 303px; }
  .learner-plate {
    position: absolute;
    left: 1025px;
    top: 615px;
    width: 120px;
    height: 120px;
  }
</style>
</head>
<body>
<main class="card">
  <div class="road-scene" role="img" aria-label="Photo of a winding coastal road curving past grassy hillside scrub"></div>

  <svg class="sweep" viewBox="0 0 1200 763" aria-hidden="true">
    <path d="M0 0 H1165 C1110 260 1010 440 800 525 C600 600 320 590 150 640 L0 700 Z" fill="var(--paper)"/>
  </svg>

  <h1 class="brand-title">Brindle Driver Training</h1>

  <table class="lesson-table">
    <thead>
      <tr>
        <th class="col-lesson">Next lesson</th>
        <th class="col-date">Date</th>
        <th class="col-time">Time</th>
      </tr>
    </thead>
    <tbody>
      <tr><td></td><td></td><td></td></tr>
      <tr><td></td><td></td><td></td></tr>
      <tr><td></td><td></td><td></td></tr>
      <tr><td></td><td></td><td></td></tr>
      <tr><td></td><td></td><td></td></tr>
      <tr><td></td><td></td><td></td></tr>
    </tbody>
  </table>

  <svg class="learner-plate" viewBox="0 0 120 120" role="img" aria-label="Learner driver L plate">
    <rect x="21" y="21" width="78" height="78" transform="rotate(45 60 60)" fill="var(--plate-yellow)" stroke="var(--ink)" stroke-width="1.5"/>
    <path d="M48 38 H58 V72 H76 V81 H48 Z" fill="var(--ink)"/>
  </svg>
</main>
</body>
</html>
```